An eCommerce Business Needs a Wordpress Web Design and Development

We need a website design and development for a new eCommerce business based in New York called "Velvet Orra". We sell items that are based on satisfying multi-sensory pathways of the person, as we believe that all is interconnected forming the Universal Language. All our products are made of raw natural elements from earth or the cosmos. The final design should communicate visual-perceptive pathways that produce harmonious effects and creativity.
Updates

Dear Designers, Please accept my sincere apology for my delayed response. I am currently in the midst of extensive business travelling while at the same time gathering feedback from online polling with friends as the website potential end-users. I shall get back to you by May 12 or sooner. Thank you for your understanding.

Target Market(s)

Art, fossils, minerals and numismatic collectors.

Industry/Entity Type

Online Shopping

Coding

Coded - Design and coding required

Number of Pages Required

5+ page

Font styles to use
Sans Serif
Script

Colors

Designer to choose colors to be used in the design.

Requirements
Must have
• - Simple and clean design.
• - Desktop and mobile device friendly.
• - Photos and images of string musical instruments, crystals, numismatics and cultural artefacts.
• - A blog page.
• - A check-out cart for online shopping and payment. Example: https://store.plumwick.com
• - Standard links to social media.

```html
<!DOCTYPE html>
<html lang="en">
<head>
<meta charset="utf-8">
<title>Velvet Orra — Blog</title>
<link rel="stylesheet" href="https://fonts.googleapis.com/css2?family=Lato:wght@400;700;900&family=Dancing+Script:wght@700&family=Crimson+Text:wght@400;600&display=swap">
<style>
:root{
  --navy:#0f2a8a;
  --blue:#1d3f9a;
  --bar-a:#2a5a9a;
  --bar-b:#0b3f8f;
  --gold:#b3932f;
  --gold-soft:#c9ad55;
  --star:#f7c93b;
  --ink:#1f2f6e;
  --dark:#0a0a0c;
  --white:#ffffff;
}
*{margin:0;padding:0;box-sizing:border-box}
html,body{width:697px;height:1200px;overflow:hidden;background:var(--white)}
body{position:relative;font-family:'Lato',sans-serif;color:var(--ink)}
.abs{position:absolute}

/* header */
.brand{left:96px;top:4px;width:68px;height:68px;border:1.5px dotted var(--gold);border-radius:50%;display:flex;align-items:center;justify-content:center;text-align:center;font-weight:700;font-size:12px;line-height:13px;color:var(--blue);letter-spacing:1px}
.search{left:238px;top:28px;width:126px;height:15px;border:2px solid var(--blue);border-radius:3px;font-size:7px;color:#aab;padding:2px 6px}
.search-btn{right:-2px;top:-2px;width:15px;height:15px;background:var(--blue);border-radius:0 3px 3px 0}
.top-nav{right:93px;top:18px;display:flex;gap:13px;font-size:6.5px;color:var(--blue)}
.top-nav .on{color:var(--gold)}
.social{display:flex;gap:8px}
.social span{width:13px;height:13px;border-radius:50%;background:var(--gold);display:block}
.head-social{left:484px;top:51px}
.cart{left:564px;top:50px}
.cart-total{left:588px;top:49px;font-size:6px;color:var(--gold);text-align:center;line-height:9px}

/* main nav */
.main-nav{left:0;top:75px;width:697px;height:27px;background:linear-gradient(90deg,var(--bar-a),var(--bar-b));display:flex;align-items:center;font-size:7px;font-weight:900;color:var(--white);letter-spacing:.3px}
.main-nav span{position:absolute}
.main-nav .on{color:var(--gold-soft)}
.dropdown{left:166px;top:102px;width:76px;height:45px;background:var(--white);font-size:5.5px;color:var(--gold);line-height:10px;padding:6px 0 0 11px;z-index:3;font-weight:700}

/* hero */
.hero{left:0;top:102px;width:697px;height:254px;background:radial-gradient(ellipse at 50% 55%,#3a3a3e 0%,#151517 55%,#050506 100%)}
.hero-curve{left:0;top:336px}
.slide{border:1px solid var(--gold);background:linear-gradient(135deg,#3c3c40 0%,#8a8a8e 45%,#2a2a2d 60%,#56565a 100%);font-family:'Crimson Text',serif;color:var(--white)}
.slide .pic{position:absolute;background:linear-gradient(180deg,#2b2b2b,#0c0c0c)}
.slide .cta{position:absolute;background:var(--white);border:1px solid var(--gold);color:#222;font-size:6px;letter-spacing:.5px;text-align:center;font-weight:600}
.slide em{font-style:normal;color:var(--gold-soft)}
.sale{left:428px;top:124px}
.dots{left:333px;top:317px;display:flex;gap:3px}
.dots i{width:6px;height:6px;border:1.5px solid var(--gold);border-radius:50%;display:block}

/* blog */
.blog-title{left:0;top:380px;width:697px;text-align:center;font-family:'Dancing Script',cursive;font-size:21px;color:var(--gold)}
.rule{top:398px;height:1px;background:var(--gold-soft)}
.card{width:156px;height:206px;border:1.5px solid var(--blue);text-align:center}
.card .pic{position:absolute;left:6px;top:-50px;width:146px;height:124px}
.card h3{position:absolute;top:78px;left:0;width:100%;font-size:8px;font-weight:900;color:var(--navy);letter-spacing:.3px}
.card p{position:absolute;top:94px;left:14px;width:126px;font-size:5.5px;font-weight:700;line-height:7.5px;color:var(--navy)}
.card .more{position:absolute;top:126px;left:40px;width:80px;height:19px;background:var(--navy);color:var(--white);font-size:6px;font-weight:900;line-height:19px}
.card .date{position:absolute;top:162px;left:0;width:100%;font-size:7px;font-weight:700;color:var(--navy)}
.card .stars{position:absolute;top:176px;left:42px}
.show-more{left:313px;top:990px;font-size:7.5px;font-weight:900;color:var(--navy)}
.reload{left:367px;top:985px}

/* footer */
.footer{left:0;top:1048px;width:697px;height:152px;background:radial-gradient(ellipse at 45% 30%,#3b1526 0%,#141015 40%,#060607 100%)}
.foot-nav{left:0;top:1086px;width:697px;display:flex;justify-content:center;gap:9px;font-family:'Crimson Text',serif;font-size:6.5px;color:var(--white)}
.foot-nav .on{color:var(--gold-soft)}
.foot-social{left:321px;top:1112px}
.foot-social span{background:var(--white)}
</style>
</head>
<body>

<header>
  <div class="abs brand">VELVET<br>ORRA</div>
  <div class="abs search">search<div class="abs search-btn"></div></div>
  <nav class="abs top-nav"><span>HOME</span><span>STORE</span><span>NEED HELP?</span><span class="on">BLOG</span><span>CONTACT</span><span>LOG IN</span></nav>
  <div class="abs social head-social" aria-label="Social links"><span></span><span></span><span></span></div>
  <svg class="abs cart" width="18" height="16" viewBox="0 0 18 16" aria-label="Cart"><path d="M1 5h16l-2 10H3z" fill="#b3932f"/><path d="M5 5l4-4 4 4" stroke="#b3932f" stroke-width="1.5" fill="none"/></svg>
  <div class="abs cart-total">200 $<br>3</div>
</header>

<nav class="abs main-nav">
  <span class="on" style="left:130px">MUSICAL INSTRUMENTS ⌄</span>
  <span style="left:242px">CRYSTALS ⌄</span>
  <span style="left:304px">NUMISMATIC COLLECTIBLES</span>
  <span style="left:429px">CULTURAL ARTIFACTS</span>
  <span style="left:531px">ABOUT US</span>
</nav>
<div class="abs dropdown">GUITAR<br>VIOLIN<br>PIANO</div>

<section class="abs hero" role="img" aria-label="Dark stage backdrop with guitar strings and glossy spheres"></section>
<svg class="abs hero-curve" width="697" height="22" viewBox="0 0 697 22"><path d="M0 20Q348-4 697 20V22H0z" fill="#fff"/></svg>

<div class="abs slide" style="left:95px;top:185px;width:122px;height:91px">
  <div class="pic" role="img" aria-label="Acoustic wood guitar" style="left:12px;top:6px;width:22px;height:78px;background:linear-gradient(180deg,#3a2a18,#c97a22 70%,#6a3a10)"></div>
  <div class="abs" style="left:68px;top:28px;font-size:6px">Wood <em>Guitar</em></div>
  <div class="abs" style="left:54px;top:37px;font-size:5.5px">10% off Only <em>This Week</em></div>
  <div class="cta" style="left:57px;top:50px;width:54px;height:15px;line-height:14px">SHOP NOW</div>
</div>

<div class="abs slide" style="left:234px;top:133px;width:228px;height:171px">
  <div class="pic" role="img" aria-label="Black electric guitar" style="left:30px;top:12px;width:60px;height:150px;background:linear-gradient(180deg,#1a1a1a,#000 60%,#333)"></div>
  <div class="abs" style="left:126px;top:56px;font-size:10px">Luxurious <em>Guitar</em></div>
  <div class="abs" style="left:138px;top:72px;font-size:11px">20% <em>Off</em></div>
  <div class="cta" style="left:110px;top:99px;width:103px;height:20px;line-height:19px;font-size:7px">SHOP NOW</div>
</div>
<svg class="abs sale" width="50" height="50" viewBox="0 0 50 50"><polygon points="25,1 31,12 44,8 39,20 49,25 39,30 44,42 31,38 25,49 19,38 6,42 11,30 1,25 11,20 6,8 19,12" fill="#f5d634" stroke="#d9b019"/><text x="25" y="28" text-anchor="middle" font-family="Lato,sans-serif" font-size="8" font-weight="700" fill="#7a5a10">Sale</text></svg>

<div class="abs slide" style="left:480px;top:185px;width:122px;height:91px">
  <div class="pic" role="img" aria-label="Blue electric guitar" style="left:12px;top:8px;width:22px;height:76px;background:linear-gradient(180deg,#1b3d8a,#2f6ad0 70%,#163070)"></div>
  <div class="abs" style="left:68px;top:28px;font-size:6px">Magic <em>Guitar</em></div>
  <div class="abs" style="left:54px;top:37px;font-size:5.5px">50% off Only <em>This Week</em></div>
  <div class="cta" style="left:57px;top:50px;width:54px;height:15px;line-height:14px">SHOP NOW</div>
</div>
<div class="abs dots"><i></i><i></i><i></i></div>

<main>
  <div class="abs rule" style="left:222px;width:100px"></div>
  <h2 class="abs blog-title">Blog</h2>
  <div class="abs rule" style="left:374px;width:104px"></div>

  <!-- row 1 -->
  <article class="abs card" style="left:94px;top:484px">
    <div class="pic" role="img" aria-label="Bronze Korean statue" style="background:linear-gradient(135deg,#2a2620,#6d6250 50%,#1c1a16)"></div>
    <h3>SILLA</h3><p>Celebrating the art of Korea's Golden Kindom</p>
    <div class="more">READ MORE</div><div class="date">Updated: 4-12-2018</div>
    <svg class="stars" width="72" height="11"><use href="#s"/><use href="#s" x="15"/><use href="#s" x="30"/><use href="#s" x="45"/><use href="#s" x="60"/></svg>
  </article>
  <article class="abs card" style="left:270px;top:484px">
    <div class="pic" role="img" aria-label="Crowd silhouetted under golden stars" style="background:radial-gradient(ellipse at 65% 70%,#e08a2a,#3a1c08 45%,#050302)"></div>
    <h3>CELEBRATING</h3><p>Celebrating the art of Korea's Golden Kindom</p>
    <div class="more">READ MORE</div><div class="date">Updated: 4-12-2018</div>
    <svg class="stars" width="72" height="11"><use href="#s"/><use href="#s" x="15"/><use href="#s" x="30"/><use href="#s" x="45"/><use href="#s" x="60"/></svg>
  </article>
  <article class="abs card" style="left:446px;top:484px">
    <div class="pic" role="img" aria-label="Polished crystals on a wooden slice" style="background:linear-gradient(160deg,#b79e86,#d8c6b4 50%,#8f7460)"></div>
    <h3>KNOW YOUR CRYSRALS</h3><p>Knowing your crystals is very important</p>
    <div class="more">READ MORE</div><div class="date">Updated: 4-12-2018</div>
    <svg class="stars" width="72" height="11"><use href="#s"/><use href="#s" x="15"/><use href="#s" x="30"/><use href="#s" x="45"/><use href="#s" x="60"/></svg>
  </article>

  <!-- row 2 -->
  <article class="abs card" style="left:94px;top:757px">
    <div class="pic" role="img" aria-label="Stone seated statue in a garden" style="background:linear-gradient(135deg,#c24a2a,#4e5a6c 45%,#3a4a2a)"></div>
    <h3>SILLA</h3><p>Celebrating the art of Korea's Golden Kindom</p>
    <div class="more">READ MORE</div><div class="date">Updated: 4-12-2018</div>
    <svg class="stars" width="72" height="11"><use href="#s"/><use href="#s" x="15"/><use href="#s" x="30"/><use href="#s" x="45"/><use href="#s" x="60"/></svg>
  </article>
  <article class="abs card" style="left:270px;top:757px">
    <div class="pic" role="img" aria-label="Violin in light trails on black" style="background:linear-gradient(135deg,#050505,#3a2214 50%,#0a0a0a)"></div>
    <h3>MAGIC OF A VIOLIN</h3><p>Celebrating the art of Korea's Golden Kindom</p>
    <div class="more">READ MORE</div><div class="date">Updated: 4-12-2018</div>
    <svg class="stars" width="72" height="11"><use href="#s"/><use href="#s" x="15"/><use href="#s" x="30"/><use href="#s" x="45"/><use href="#s" x="60"/></svg>
  </article>
  <article class="abs card" style="left:446px;top:757px">
    <div class="pic" role="img" aria-label="Stacked gold coins" style="background:linear-gradient(135deg,#7a5418,#d3a24a 50%,#e8e2d6)"></div>
    <h3>NUMISMATIC COLLECTIONS</h3><p>Our numismatic collectibles coins speak for themselves.</p>
    <div class="more">READ MORE</div><div class="date">Updated: 4-12-2018</div>
    <svg class="stars" width="72" height="11"><use href="#s"/><use href="#s" x="15"/><use href="#s" x="30"/><use href="#s" x="45"/><use href="#s" x="60"/></svg>
  </article>

  <div class="abs show-more">Show More</div>
  <svg class="abs reload" width="18" height="18" viewBox="0 0 18 18"><path d="M9 3a6 6 0 1 1-6 6" stroke="#1d3f9a" stroke-width="2" fill="none"/><path d="M9 0v6L5 3z" fill="#1d3f9a"/></svg>
</main>

<footer>
  <div class="abs footer" role="img" aria-label="Dark crystal and concert-light backdrop"></div>
  <nav class="abs foot-nav"><span>HOME</span><span>STORE</span><span>NEED HELP?</span><span class="on">BLOG</span><span>CONTACT</span><span>LOG IN</span></nav>
  <div class="abs social foot-social" aria-label="Social links"><span></span><span></span><span></span></div>
</footer>

<svg width="0" height="0" style="position:absolute"><defs><polygon id="s" points="6,0 7.6,3.8 11.7,4.1 8.6,6.8 9.5,10.8 6,8.7 2.5,10.8 3.4,6.8 0.3,4.1 4.4,3.8" fill="#f7c93b"/></defs></svg>
</body>
</html>
```